Design a Website Mockup for Sunlit Orchard

My website is being programmed right now, but I have no design for it. We do have a template ... it is Palquist from BrixLayouts. I need a color scheme, a header layout, a footer layout, and all of the "look and feel" elements. And I need it rather quickly!

I do have a logo already, although the colors on the logo are not set in stone. You can change those if you like.

The concept of the website is a photo scanning service that serves the USA and Canada (mostly the US). As such, I would like it to have a slightly patriotic feel to it. A visitor to the website should feel drawn into the site.

Please ask questions! This is a high priority and I need to get it done.

Added 3-17-2015: I added the wireframes in PPT to this contest.
Dorian

```html
<!DOCTYPE html>
<html lang="en">
<head>
<meta charset="utf-8">
<title>Sunlit Orchard — Photo Scanning</title>
<link rel="stylesheet" href="https://fonts.googleapis.com/css2?family=Archivo:wdth,wght@62..125,200..900&family=Open+Sans:wght@400;600;700&family=Oswald:wght@500&family=Pacifico&family=Roboto+Condensed:wght@700&display=swap">
<style>
:root{
  --navy:#3e5672;
  --tan:#b7a57c;
  --tan-light:#c6b58f;
  --brick:#ad432d;
  --ink:#333;
  --topbar:#f4f2ed;
  --footer:#413b36;
  --footer-line:#534c46;
  --footer-text:#e9e5df;
  --white:#fff;
}
*{margin:0;padding:0;box-sizing:border-box}
html,body{width:1094px;height:1200px;overflow:hidden;background:var(--white)}
body{position:relative;font-family:"Open Sans",Arial,sans-serif;color:var(--ink)}
a{text-decoration:none;color:inherit}

/* top bar */
.topbar{position:absolute;top:0;left:0;width:1094px;height:33px;background:var(--topbar);border-top:3px solid #2d2a27;font-size:11px;color:#555}
.topbar .account-links{position:absolute;left:113px;top:8px;display:flex;gap:22px}
.topbar .account-links span::before{content:"";display:inline-block;width:9px;height:9px;background:var(--tan);border-radius:2px;margin-right:6px;vertical-align:-1px}
.topbar .welcome{position:absolute;left:692px;top:8px}
.topbar .auth{position:absolute;left:808px;top:8px}
.topbar .auth a{color:var(--tan)}
.topbar .lang{position:absolute;left:911px;top:3px;width:69px;height:27px;background:var(--tan);color:var(--white);font-weight:700;font-size:11px;line-height:27px;text-align:center}

/* header */
.header{position:absolute;top:33px;left:0;width:1094px;height:81px;background:var(--white)}
.brand{position:absolute;left:108px;top:24px;display:flex;align-items:center;gap:8px}
.brand .mark{width:20px;height:20px;background:var(--navy)}
.brand .name{font-family:"Archivo",Arial,sans-serif;font-weight:800;font-size:15px;color:var(--navy)}
.main-nav{position:absolute;left:237px;top:45px;display:flex;gap:20px;font-family:"Roboto Condensed","Arial Narrow",sans-serif;font-weight:700;font-size:14.5px;color:var(--navy);white-space:nowrap}
.main-nav .current{color:var(--tan)}
.search{position:absolute;left:817px;top:40px;width:162px;height:27px;border:1px solid #ddd;font-size:11px;color:#999;padding:6px 7px;background:var(--white)}
.search svg{position:absolute;right:6px;top:6px}
.dropdown{position:absolute;left:524px;top:101px;width:130px;z-index:3}
.dropdown div{height:33px;margin-bottom:3px;background:var(--navy);border:2px solid #6c819a;outline:1px solid var(--navy);color:var(--tan-light);font-family:"Roboto Condensed","Arial Narrow",sans-serif;font-weight:700;font-size:14px;line-height:29px;padding-left:10px}

/* hero */
.hero{position:absolute;top:114px;left:0;width:1094px;height:342px}
.hero .photo{position:absolute;inset:0;background:linear-gradient(100deg,#d9c3a8 0%,#e9ddcb 30%,#f3eee6 55%,#f6f4f0 100%)}
.hero .headline{position:absolute;left:521px;top:54px;font-family:"Archivo",Arial,sans-serif;font-weight:900;font-stretch:70%;font-size:100px;letter-spacing:-2px;line-height:1;color:var(--navy)}
.hero .subline{position:absolute;left:520px;top:136px;font-family:"Archivo",Arial,sans-serif;font-weight:200;font-size:64px;letter-spacing:-1px;line-height:1;color:var(--navy)}
.hero .tagline{position:absolute;left:815px;top:196px;font-family:"Pacifico",cursive;font-size:21px;color:var(--white);transform:rotate(-4deg)}

/* feature blocks */
.features{position:absolute;top:456px;left:0;width:1094px;height:352px;display:flex}
.feature{width:365px;position:relative}
.feature+.feature::before{content:"";position:absolute;left:0;top:101px;width:3px;height:200px;background:#ece8e0}
.feature .banner{height:101px;padding:6px 4px;position:relative}
.feature .banner div{height:100%;border:1px solid rgba(255,255,255,.35);display:flex;align-items:center;justify-content:center;font-family:"Archivo",Arial,sans-serif;font-weight:800;font-stretch:80%;font-size:38px;color:var(--white);letter-spacing:-.5px}
.feature.do .banner{background:var(--navy)}
.feature.get .banner{background:var(--tan)}
.feature.matters .banner{background:var(--brick)}
.steps{list-style:none;padding:14px 15px 0}
.steps li{font-family:"Archivo",Arial,sans-serif;font-weight:800;font-stretch:85%;font-size:16px;color:var(--tan-light);height:29px;display:flex;align-items:center;gap:7px}
.steps li b{width:19px;height:19px;border-radius:50%;background:var(--tan-light);color:var(--white);font-size:12px;display:flex;align-items:center;justify-content:center}
.copy{padding:6px 15px 0;font-size:11px;line-height:11px;color:#a5a5a5}
.copy p{margin-bottom:15px}

/* footer */
.footer{position:absolute;top:808px;left:0;width:1094px;height:392px;background:var(--footer);color:var(--footer-text)}
.footer h3{font-family:"Oswald",Arial,sans-serif;font-weight:500;font-size:17px;color:var(--white);margin-bottom:20px}
.fcol{position:absolute;top:62px}
.fcol ul{list-style:none;font-size:11px}
.fcol li{height:27.4px}
.fcol li::before{content:"";display:inline-block;width:4px;height:4px;background:var(--tan);margin-right:8px;vertical-align:2px}
.links{left:113px}.info{left:335px}
.chirp{left:558px;width:195px;font-size:11px;line-height:17px}
.chirp .arrows{position:absolute;right:0;top:2px;font-size:15px;letter-spacing:10px}
.chirp a{color:var(--tan)}
.chirp em{display:block;font-size:9px;margin-bottom:12px}
.friends{left:780px;width:180px;font-size:11px}
.friends .like{position:absolute;left:110px;top:0;width:60px;height:18px;background:var(--tan);color:var(--white);font-weight:700;font-size:10px;text-align:center;line-height:18px;border-radius:2px}
.friends .count a{color:var(--tan)}
.avatars{display:grid;grid-template-columns:repeat(3,46px);gap:12px 21px;margin-top:10px;font-size:10px;text-align:center}
.avatars span{display:block;width:46px;height:46px;margin-bottom:5px;background:linear-gradient(#8c7d6e,#5e554d)}
.avatars .blank{background:#cfd3d8}
.fbottom{position:absolute;top:335px;left:0;width:1094px;border-top:1px solid var(--footer-line)}
.social{position:absolute;left:113px;top:15px;display:flex;gap:11px}
.social span{width:26px;height:26px;background:#5d5650;border-radius:2px}
.copyright{position:absolute;left:788px;top:23px;font-size:10px}
.to-top{position:absolute;left:1055px;top:21px;width:27px;height:27px;background:var(--tan);display:flex;align-items:center;justify-content:center}
</style>
</head>
<body>

<div class="topbar">
  <div class="account-links"><span>My Account</span><span>My Wishlist</span><span>Cart</span><span>Checkout</span></div>
  <div class="welcome">Welcome message!</div>
  <div class="auth"><a href="#">Login</a> or <a href="#">Register</a></div>
  <div class="lang">English</div>
</div>

<header class="header">
  <div class="brand"><span class="mark"></span><span class="name">Sunlit Orchard</span></div>
  <nav class="main-nav">
    <a class="current" href="#">PATRIOTIC MISSION</a>
    <a href="#">SERVICES &amp; PRODUCTS</a>
    <a href="#">PROCESS</a>
    <a href="#">PRICING</a>
    <a href="#">ABOUT US</a>
    <a href="#">CONTACT</a>
  </nav>
  <div class="search">Search here
    <svg width="14" height="14" viewBox="0 0 14 14"><circle cx="6" cy="6" r="4.5" fill="none" stroke="#b7a57c" stroke-width="2"/><line x1="9.3" y1="9.3" x2="13" y2="13" stroke="#b7a57c" stroke-width="2"/></svg>
  </div>
</header>

<div class="dropdown"><div>SAFETY</div><div>CARE</div></div>

<section class="hero">
  <div class="photo" role="img" aria-label="Photo of a laughing family carrying children on a sunny beach with colourful balloons"></div>
  <div class="headline">Momories</div>
  <div class="subline">That last a life time.</div>
  <div class="tagline">yes that is our business!</div>
</section>

<section class="features">
  <div class="feature do">
    <div class="banner"><div>What we do.</div></div>
    <ol class="steps"><li><b>1</b>Select your lorem ipsum</li><li><b>2</b>Upload photo.</li><li><b>3</b>Procced to payment.</li></ol>
    <div class="copy"><p>Lorem ipsum dolor sit amet,</p><p>consectetur adipiscing elit, sed do eiusmod tempor incididunt ut labore et dolore magna aliqua. Ut enim ad minim veniam, quis nostrud exercitation ullamco laboris nisi ut aliquip ex ea commodo consequat.</p><p>Duis aute irure dolor in reprehenderit in voluptate velit esse cillum dolore eu fugiat nulla pariatur. Excepteur sint occaecat cupidatat non proident, sunt in culpa qui officia deserunt mollit anim id est laborum.</p></div>
  </div>
  <div class="feature get">
    <div class="banner"><div>What you get.</div></div>
    <ol class="steps"><li><b>1</b>Select your lorem ipsum</li><li><b>2</b>Upload photo.</li><li><b>3</b>Procced to payment.</li></ol>
    <div class="copy"><p>Lorem ipsum dolor sit amet,</p><p>consectetur adipiscing elit, sed do eiusmod tempor incididunt ut labore et dolore magna aliqua. Ut enim ad minim veniam, quis nostrud exercitation ullamco laboris nisi ut aliquip ex ea commodo consequat.</p><p>Duis aute irure dolor in reprehenderit in voluptate velit esse cillum dolore eu fugiat nulla pariatur. Excepteur sint occaecat cupidatat non proident, sunt in culpa qui officia deserunt mollit anim id est laborum.</p></div>
  </div>
  <div class="feature matters">
    <div class="banner"><div>Why it matters.</div></div>
    <ol class="steps"><li><b>1</b>Select your lorem ipsum</li><li><b>2</b>Upload photo.</li><li><b>3</b>Procced to payment.</li></ol>
    <div class="copy"><p>Lorem ipsum dolor sit amet,</p><p>consectetur adipiscing elit, sed do eiusmod tempor incididunt ut labore et dolore magna aliqua. Ut enim ad minim veniam, quis nostrud exercitation ullamco laboris nisi ut aliquip ex ea commodo consequat.</p><p>Duis aute irure dolor in reprehenderit in voluptate velit esse cillum dolore eu fugiat nulla pariatur. Excepteur sint occaecat cupidatat non proident, sunt in culpa qui officia deserunt mollit anim id est laborum.</p></div>
  </div>
</section>

<footer class="footer">
  <div class="fcol links"><h3>LINKS</h3>
    <ul><li>My Account</li><li>Personal information</li><li>Addresses</li><li>Discount</li><li>Order History</li><li>Your Vouchers</li></ul>
  </div>
  <div class="fcol info"><h3>INFORMATION</h3>
    <ul><li>New products</li><li>Top sellers</li><li>Specials</li><li>Manufacturers</li><li>Suppliers</li><li>Our stores</li></ul>
  </div>
  <div class="fcol chirp"><h3>FROM CHIRPLINE</h3><span class="arrows">‹ ›</span>
    <p>Checkout this new Top Selling Shopwell theme in 2015, has all your needs. <a href="#">http://sn.ip/k8Qw2Lr4ZT</a></p><em>about 6 days ago</em>
    <p>Check out 'Rekindle - Multi-Purpose Responsive PressKit Theme' on #CraftBazaar by <a href="#">@quietharbor52</a> #layoutfair <a href="#">http://sn.ip/Vd7pXe3NcB</a></p><em>about 7 days ago</em>
  </div>
  <div class="fcol friends"><h3>FRIENDWALL</h3><span class="like">Like!</span>
    <div class="count">2,727 people like <a href="#">Tallowby Co.</a></div>
    <div class="avatars">
      <div><span role="img" aria-label="Profile photo"></span>Hollis</div>
      <div><span class="blank" role="img" aria-label="Empty profile placeholder"></span>Marisol</div>
      <div><span role="img" aria-label="Profile photo"></span>Benedet...</div>
      <div><span role="img" aria-label="Profile photo"></span>Tobias</div>
      <div><span role="img" aria-label="Profile photo"></span>Ravindra</div>
      <div><span role="img" aria-label="Profile photo"></span>Odette</div>
    </div>
  </div>
  <div class="fbottom">
    <div class="social"><span></span><span></span><span></span><span></span><span></span><span></span><span></span><span></span><span></span></div>
    <div class="copyright">© 2014 Palquist Store. All Rights Reserved.</div>
    <a class="to-top" href="#"><svg width="12" height="8" viewBox="0 0 12 8"><polyline points="1,7 6,2 11,7" fill="none" stroke="#fff" stroke-width="2"/></svg></a>
  </div>
</footer>

</body>
</html>
```